Updated Business Card for Optometry Practice

We're a growing optometry practice that is moving to a beautiful new office and we want to update our business card. We just updated our logo so the new card should reflect the new logo. Our practice continually invests in state of the art instruments to help us provide eye care that is thorough, comfortable, efficient and educational.

I've attached our current card and logo. You can reference this for the information I would like on the card. The tag line on the back is "We're changing the way you see."

Upon completion of this project we will need (amongst other formats) Photoshop files of the card so I can change employee names to print cards for each employee.

```html
<!DOCTYPE html>
<html lang="en">
<head>
<meta charset="utf-8">
<title>Brightwater Family Eyecare – Business Card</title>
<link href="https://fonts.googleapis.com/css2?family=Montserrat:wght@400;500;600;700&display=swap" rel="stylesheet">
<style>
  :root {
    --navy: #15294f;
    --gold: #d8b22c;
    --white: #ffffff;
    --ink: #1b1b1b;
    --stage: #2b2b2b;
  }
  * { box-sizing: border-box; margin: 0; padding: 0; }
  html, body { width: 1200px; height: 711px; overflow: hidden; }
  body {
    background: var(--stage);
    font-family: "Montserrat", sans-serif;
    display: flex;
    align-items: center;
    justify-content: center;
    gap: 40px;
  }
  .card {
    position: relative;
    width: 540px;
    height: 309px;
    border-radius: 22px;
    overflow: hidden;
  }
  /* Front */
  .card--front {
    background: var(--navy);
    display: flex;
    align-items: center;
    justify-content: center;
  }
  .brand {
    display: flex;
    align-items: center;
    gap: 12px;
    font-weight: 600;
    letter-spacing: 0.08em;
    text-transform: uppercase;
  }
  .brand__dot {
    border-radius: 50%;
    background: var(--gold);
    flex: none;
  }
  .card--front .brand { color: var(--white); font-size: 24px; }
  .card--front .brand__dot { width: 22px; height: 22px; }

  /* Back */
  .card--back { background: var(--white); }
  .back__swoosh { position: absolute; inset: 0; }
  .back__brand {
    position: absolute;
    left: 26px;
    top: 118px;
  }
  .card--back .brand { color: var(--navy); font-size: 12.5px; gap: 8px; line-height: 1.25; }
  .card--back .brand__dot { width: 14px; height: 14px; }
  .back__divider {
    position: absolute;
    left: 222px;
    top: 40px;
    width: 1.5px;
    height: 150px;
    background: var(--gold);
  }
  .contact {
    position: absolute;
    left: 240px;
    top: 34px;
    color: var(--ink);
    font-size: 11.5px;
    line-height: 1.45;
  }
  .contact__name {
    font-size: 16px;
    font-weight: 700;
    color: var(--navy);
    letter-spacing: 0.01em;
  }
  .contact__name span { color: var(--gold); }
  .contact__title { color: var(--gold); font-size: 12px; margin-bottom: 6px; }
  .contact__address { margin-bottom: 6px; font-weight: 500; }
  .contact__line { display: flex; align-items: center; gap: 7px; font-weight: 500; }
  .contact__icon { width: 11px; height: 11px; flex: none; }
</style>
</head>
<body>
  <section class="card card--front" aria-label="Card front">
    <div class="brand"><span class="brand__dot"></span>Brightwater Family Eyecare</div>
  </section>

  <section class="card card--back" aria-label="Card back">
    <svg class="back__swoosh" width="540" height="309" viewBox="0 0 540 309" aria-hidden="true">
      <path d="M0 309 L0 278 Q300 268 540 190 L540 309 Z" fill="var(--navy)"/>
      <path d="M30 268 Q300 254 520 182" fill="none" stroke="var(--gold)" stroke-width="4" stroke-linecap="round"/>
    </svg>

    <div class="back__brand">
      <div class="brand"><span class="brand__dot"></span>Brightwater<br>Family Eyecare</div>
    </div>

    <div class="back__divider"></div>

    <div class="contact">
      <div class="contact__name">DANIEL <span>MARSH, OD</span></div>
      <div class="contact__title">Optometrist</div>
      <div class="contact__address">
        Brightwater Family Eyecare<br>
        2870 Linden Park Way #210<br>
        Brightwater, MO 63000
      </div>
      <div class="contact__line">
        <svg class="contact__icon" viewBox="0 0 12 12" aria-hidden="true"><path d="M2.5 1 L4.5 1 L5.3 3.4 L4 4.4 Q5 6.8 7.6 8 L8.6 6.7 L11 7.5 L11 9.5 Q10.5 11 9 11 Q1 10 1 3 Q1 1.5 2.5 1 Z" fill="var(--gold)"/></svg>
        (555) 018-2741
      </div>
      <div class="contact__line">
        <svg class="contact__icon" viewBox="0 0 12 12" aria-hidden="true"><rect x="0.5" y="2.5" width="11" height="7.5" rx="1" fill="var(--gold)"/><path d="M0.8 3 L6 7 L11.2 3" fill="none" stroke="var(--white)" stroke-width="1"/></svg>
        dan@brightwatereyecare.com
      </div>
      <div class="contact__line">
        <svg class="contact__icon" viewBox="0 0 12 12" aria-hidden="true"><circle cx="6" cy="6" r="5.3" fill="var(--gold)"/><path d="M0.8 6 H11.2 M6 0.7 Q3 6 6 11.3 M6 0.7 Q9 6 6 11.3" fill="none" stroke="var(--white)" stroke-width="0.8"/></svg>
        www.brightwatereyecare.com
      </div>
    </div>
  </section>
</body>
</html>
```